Harborview Sight Fellowship Hall needs an ad/flyer for convention program

Established in 1949, the Harborview Sight Fellowship Hall's mission is to enrich the lives of blind and visually impaired adults by preparing them for a normal, active life in a society that is principally sighted by encouraging independence.

Located in Quillmont Green in San Diego, California, we are a nonprofit that gives blind and visually impaired people in our community an opportunity to socialize and interact. We help members build skills, confidence, and self-esteem through our various social, recreational, and educational activities. We were founded partially by Otter Society members and receive ongoing funding from them.

We need an 8 1/2 by 11 inch color ad in jpg format. We would like it to be editable. This will be the foundation of our rebranding. The ad will be in a meeting program of the California Otters (californiaotters-example.org) with the goal of highlighting some of our programs in order to solicit donations from individual Otter Societies, preferably ongoing ones.

We would like the ad to be generic enough that we can use the ad for other events and as a flyer in the future. We want the ad/flyer to be classic but eye popping with color. We want the design to reflect a professional and lively organization that loves to serve our members. We don’t entirely love our logo, but it’s what we have for now. Our next task will be a new logo design.

We would like to highlight some of our programs for our members include bingo, blind waterskiing and surfing, cooking and ceramic classes, foreign language classes, self defense classes, yoga, and craft classes. Many of the crafts our members make are sold during fundraisers, and they include blankets, scarves, beaded animals, and more. See a sampling of pictures. We provide transportation to and from our Center, free lunch while at the Center, and food to take home. Many of these activities continue during the pandemic via online platforms. We are doing monthly home deliveries of food to our members.

We need donations to keep our programs going, and we have building repairs & maintenance that we need donations in order to complete. See attached document regarding donations. Please reach out if you have questions. Thank you.

Web address: hvsfh-example.org
Street address: The Harborview Sight Fellowship Hall, 4472 Marrow Ln San Diego, CA 92188
Email address: donation@hvsfh-example.org
To make a donation: https://hvsfh-example.org/donate-2/

Target Market(s)

Donors

Industry/Entity Type

NonProfit

Font styles to use
Sans Serif

Requirements
Must have
• Highlight programs and information on how to make a donation.
Nice to have
• Information on how much each dollar donated will go - see attachment
Should not have
• Unprofessional or sloppy details

```html
<!DOCTYPE html>
<html lang="en">
<head>
<meta charset="utf-8">
<title>Harborview Sight Fellowship Hall – Donation Flyer</title>
<link rel="stylesheet" href="https://fonts.googleapis.com/css2?family=Lato:wght@400;700&family=Marcellus&display=swap">
<style>
  :root{
    --navy:#30466f;
    --navy-light:#4a659c;
    --brand:#4f72b3;
    --pill:#d6e0f1;
    --band:#8fa6d1;
    --paper:#f4f5f8;
    --ink:#2b2f3a;
    --white:#ffffff;
  }
  *{margin:0;padding:0;box-sizing:border-box}
  html,body{width:800px;height:1200px;overflow:hidden;background:#fff}
  .flyer{position:relative;width:800px;height:1200px;overflow:hidden;font-family:'Lato',sans-serif;color:var(--ink)}
  .backdrop{position:absolute;inset:0}
  .brand{position:absolute;left:24px;top:28px;display:flex;align-items:center;gap:14px}
  .brand-dot{width:78px;height:78px;border:4px solid var(--brand);border-radius:50%;flex:none}
  .brand-name{font-family:'Marcellus',serif;color:var(--brand);font-size:25px;line-height:1.12;width:270px}
  .photo-circle{position:absolute;border-radius:50%;border:5px solid var(--white);box-shadow:0 0 0 3px var(--brand)}

  .giving{position:absolute;left:0;top:455px;width:440px;color:var(--white)}
  .section-title{font-family:'Marcellus',serif;font-weight:400;font-size:36px;letter-spacing:.5px}
  .giving .section-title{margin-left:28px;margin-bottom:14px}
  .tier{margin-bottom:16px}
  .tier-label{display:inline-block;background:var(--pill);color:var(--navy);font-weight:700;font-size:13px;padding:5px 26px 5px 28px;border-radius:0 14px 14px 0;min-width:282px}
  .tier ul{list-style:none;margin:8px 0 0 28px;font-size:12px;line-height:18px}
  .tier li::before{content:"•";margin-right:9px}
  .tier-note{margin:10px 0 0 28px;font-size:12px}
  .lunch-total{margin:28px 0 0 28px;width:380px;text-align:center}
  .lunch-total strong{display:block;font-weight:400;font-size:18px;letter-spacing:.3px}
  .lunch-total span{display:block;font-size:12.5px;margin-top:4px;letter-spacing:.3px}
  .lunch-total small{display:block;font-size:11px;color:#d7def0;margin-top:2px}

  .facts{position:absolute;right:0;top:625px;width:400px;text-align:right}
  .facts .section-title{color:var(--brand);font-size:38px;margin-right:18px;margin-bottom:14px}
  .fact{position:relative;padding-right:48px;font-size:12.3px;line-height:17px;margin-bottom:18px;color:var(--ink)}
  .fact .hl{color:var(--brand)}
  .fact-icon{position:absolute;right:18px;top:2px;width:14px;height:14px}

  .donate{position:absolute;right:0;top:1074px;width:400px}
  .donate-label{display:flex;justify-content:flex-end;align-items:center;gap:10px;padding-right:36px;font-size:15px;font-weight:700;color:var(--ink)}
  .donate-url{margin-top:6px;background:var(--brand);color:var(--white);font-size:17px;padding:6px 24px 6px 22px;border-radius:18px 0 0 18px;text-align:right}
  .contact{margin-top:10px;padding-right:30px;text-align:right;font-size:14px;line-height:22px;color:var(--ink)}
  .contact b{font-weight:700}
</style>
</head>
<body>
<main class="flyer">
  <svg class="backdrop" width="800" height="1200" viewBox="0 0 800 1200" aria-hidden="true">
    <defs>
      <linearGradient id="navyFill" x1="0" y1="0" x2="1" y2="1">
        <stop offset="0" stop-color="#3f5a8f"/>
        <stop offset="1" stop-color="#2d426b"/>
      </linearGradient>
      <linearGradient id="blanketFill" x1="0" y1="0" x2="1" y2="0">
        <stop offset="0" stop-color="#e2e2e2"/>
        <stop offset=".38" stop-color="#b9b9bb"/>
        <stop offset=".55" stop-color="#e98c82"/>
        <stop offset=".78" stop-color="#f2b0b8"/>
        <stop offset="1" stop-color="#9f86ad"/>
      </linearGradient>
    </defs>
    <rect width="800" height="1200" fill="url(#navyFill)"/>
    <rect x="0" y="0" width="800" height="440" fill="url(#blanketFill)"/>
    <path d="M0,0 H500 C450,140 320,215 170,228 C100,233 40,232 0,228 Z" fill="#c9ccd3"/>
    <path d="M0,0 H470 C420,125 300,195 160,210 C90,217 40,216 0,212 Z" fill="#ffffff"/>
    <path d="M0,388 C160,350 340,362 480,425 L470,1200 L0,1200 Z" fill="#eef1f8"/>
    <path d="M0,400 C160,364 340,376 470,438 L460,1200 L0,1200 Z" fill="url(#navyFill)"/>
    <path d="M800,450 L800,1200 L372,1200 C412,1010 436,820 428,640 C424,560 470,486 560,450 Z" fill="#a9bbe0"/>
    <path d="M800,460 L800,1200 L384,1200 C424,1010 446,820 438,642 C434,566 478,496 566,462 Z" fill="var(--paper)"/>
  </svg>
  <div role="img" aria-label="Photo of a chunky pink, coral and lavender knitted blanket made by members" style="position:absolute;left:330px;top:0;width:470px;height:420px"></div>

  <div class="brand">
    <span class="brand-dot"></span>
    <span class="brand-name">Harborview Sight Fellowship Hall</span>
  </div>

  <div class="photo-circle" role="img" aria-label="Photo of a beaded angel ornament made in craft class" style="left:418px;top:400px;width:174px;height:174px;background:radial-gradient(circle at 50% 40%,#c9cbd2,#5b6fa8 60%,#283d7a)"></div>
  <div class="photo-circle" role="img" aria-label="Photo of a beaded penguin with a Santa hat on a knitted scarf" style="left:594px;top:395px;width:186px;height:186px;background:radial-gradient(circle at 50% 40%,#6a6a6e,#b9b9bd 60%,#e0e0e2)"></div>

  <section class="giving">
    <h2 class="section-title">PRE-COVID:</h2>
    <div class="tier">
      <span class="tier-label">$10 PER MONTH OR $120 WILL BUY:</span>
      <ul>
        <li>60 meals for our lunch program – we serve 130 meals each week</li>
        <li>13 round trip CTS transportation tickets</li>
        <li>Enough beads to make 35 Rosa Bell angels in our craft class</li>
      </ul>
    </div>
    <div class="tier">
      <span class="tier-label">$20 PER MONTH OR $240 WILL BUY:</span>
      <ul>
        <li>26 round trip CTS transportation tickets</li>
        <li>One month of large print and Braille translation newsletter printing</li>
      </ul>
    </div>
    <div class="tier">
      <span class="tier-label">$50 PER MONTH OR $600 WILL BUY:</span>
      <ul>
        <li>300 lunches</li>
        <li>Thanksgiving dinner with all the fixings for 80 to 100 guests</li>
      </ul>
    </div>
    <div class="tier">
      <span class="tier-label">$100 PER MONTH OR $1200 WILL BUY:</span>
      <ul><li>Approximately 10 Bingo parties including food and prizes</li></ul>
    </div>
    <div class="lunch-total">
      <strong>$1,083 PER MONTH OR $13,000 PER YEAR</strong>
      <span>WILL FUND OUR ENTIRE LUNCH PROGRAM FOR THE YEAR.</span>
      <small>Every dollar donated goes to support HSFH participants and programs.</small>
    </div>
  </section>

  <div class="photo-circle" role="img" aria-label="Photo of a glazed ceramic teapot from ceramics class" style="left:28px;top:1012px;width:134px;height:134px;background:radial-gradient(circle at 45% 45%,#c98a55,#6b4a35 60%,#3c3a3e)"></div>
  <div class="photo-circle" role="img" aria-label="Photo of a grey and white knitted blanket with a thank-you card" style="left:150px;top:995px;width:156px;height:156px;background:radial-gradient(circle at 50% 50%,#e8e8ea,#8c8c92 60%,#3f3f45)"></div>
  <div class="photo-circle" role="img" aria-label="Photo of a bouquet of pink and cream flowers" style="left:292px;top:1016px;width:126px;height:126px;background:radial-gradient(circle at 50% 50%,#f6d4d2,#e9a7a9 55%,#7a8f6a)"></div>

  <section class="facts">
    <h2 class="section-title">DID YOU KNOW?</h2>
    <p class="fact">During the pandemic we offer Bingo, Trivia and other virtual<br>games every week, where blind and low vision participants can<br>win HSFH bucks. <span class="hl">You can sponsor one day of games for $35.</span>
      <svg class="fact-icon" viewBox="0 0 14 14" aria-hidden="true"><circle cx="7" cy="7" r="6" fill="none" stroke="#4f72b3" stroke-width="1.2"/><path d="M8.2,4 L5.4,7 L8.2,10" fill="none" stroke="#4f72b3" stroke-width="1.4"/></svg></p>
    <p class="fact">You can provide 75 gift bags for our ‘We are in This Together’<br>home delivery program. Many of our blind and low vision<br>people are isolated and stuck at home. These gift<br>packages are welcomed with enthusiasm and gratefulness.<br><span class="hl">Your rewards are huge smiles and happy faces.</span>
      <svg class="fact-icon" viewBox="0 0 14 14" aria-hidden="true"><circle cx="7" cy="7" r="6" fill="none" stroke="#4f72b3" stroke-width="1.2"/><path d="M8.2,4 L5.4,7 L8.2,10" fill="none" stroke="#4f72b3" stroke-width="1.4"/></svg></p>
    <p class="fact">Our building is over <span class="hl">20 years old</span> and requires<br>ongoing maintenance and repairs
      <svg class="fact-icon" viewBox="0 0 14 14" aria-hidden="true"><circle cx="7" cy="7" r="6" fill="none" stroke="#4f72b3" stroke-width="1.2"/><path d="M8.2,4 L5.4,7 L8.2,10" fill="none" stroke="#4f72b3" stroke-width="1.4"/></svg></p>
    <p class="fact">Fencing (cage) required to protect outside air conditioning<br>units from vandalism. <span class="hl">Cost: $2,500</span>
      <svg class="fact-icon" viewBox="0 0 14 14" aria-hidden="true"><circle cx="7" cy="7" r="6" fill="none" stroke="#4f72b3" stroke-width="1.2"/><path d="M8.2,4 L5.4,7 L8.2,10" fill="none" stroke="#4f72b3" stroke-width="1.4"/></svg></p>
    <p class="fact"><span class="hl">Wanted:</span> Sponsors for weekly virtual bingo and trivia games:<br>Blind and Low vision participants receive one HSFH buck per win.<br>HSFH bucks are turned into gift cards and CTS transportation<br>passes. <span class="hl">Sponsor one week for $40. Sponsor 1 month for $160</span>
      <svg class="fact-icon" viewBox="0 0 14 14" aria-hidden="true"><circle cx="7" cy="7" r="6" fill="none" stroke="#4f72b3" stroke-width="1.2"/><path d="M8.2,4 L5.4,7 L8.2,10" fill="none" stroke="#4f72b3" stroke-width="1.4"/></svg></p>
  </section>

  <section class="donate">
    <div class="donate-label">
      <svg width="34" height="14" viewBox="0 0 34 14" aria-hidden="true"><path d="M32,7 H4 M9,2 L3,7 L9,12" fill="none" stroke="#2b2f3a" stroke-width="1.6"/></svg>
      <span>TO MAKE A DONATION:</span>
    </div>
    <div class="donate-url">https://hvsfh-example.org/donate-2/</div>
    <div class="contact">
      <b>donation@hvsfh-example.org</b> | <b>www.hvsfh-example.org</b><br>
      4472 Marrow Ln San Diego, CA 92188
    </div>
  </section>
</main>
</body>
</html>
```